Fjellmoss Botanics - Black Face Mask Packaging Design

We require packaging design for a charcoal activated blackhead removal peel off face mask (please see attachment of competitors product).

1: We require a logo for our brand name: 'Fjellmoss Botanics'

2: We require a 3d rendered image of the box with the tube

3: We require label templates for both the box and the tube

The logo design brief is as follows:

We are bringing out a range of natural beauty products. We require a logo that represents norwegian natural beauty & incorporates the Norwegian Flag.

The packaging design brief is as follows:

Please attachment: (FBGen). There is an image of a woman with a black face mask.

1:We require our packaging design to have a generic face with a face mask being pulled off/stretched (as shown in the above attachment).
However, the face mask should display a Norwegian flag. The part of the mask that is still fixed to the face should be in full pastel Norwegian flag colors. The part of the mask that has been peeled away should be faded to charcoal grey (whilst maintaining the Norwegian flag). The ratio should be around 50/50 of mask attached to mask being peeled.
The colors throughout should be soft.

2:The design should also incorporate a unisex logo.(Please see attachment: FBUnisex)

3: The design should display the wording: 'Charcoal Activated Face Mask'

4: The design should also display the tagline: 'restores your youthful glow'

5: The back of the tube should display the ingredients: Please see attached. The back should also say ISO901 & GMPC certified

Please note, the packaging design for the tube should just be black and white as the printing machine on the tube can only be white.

The box can be a variation of colors as there are no restrictions on the colors for printing onto cardboard

Target Market(s)

Beauty, Natural Beauty, Unisex

Industry/Entity Type

Product

Logo Text

Fjellmoss Botanics

Requirements
Must have
• Please refer to project description
Nice to have

```html
<!DOCTYPE html>
<html lang="en">
<head>
<meta charset="utf-8">
<title>Fjellmoss Botanics – Charcoal Activated Face Mask Labels</title>
<link rel="stylesheet" href="https://fonts.googleapis.com/css2?family=Marcellus&family=Poiret+One&family=Open+Sans:wght@400;600&display=swap">
<style>
  :root {
    --bg-top: #d9d9d9;
    --bg-bottom: #bdbdbd;
    --pack-black: #050505;
    --label-white: #ffffff;
    --charcoal-panel: #4a4640;
    --panel-text: #ece8e2;
    --accent-red: #e0202a;
    --accent-blue: #1d2fd0;
    --ink: #111111;
  }
  * { box-sizing: border-box; margin: 0; padding: 0; }
  html, body { width: 1200px; height: 1156px; overflow: hidden; }
  body {
    background: linear-gradient(180deg, var(--bg-top), var(--bg-bottom));
    position: relative;
    font-family: "Open Sans", sans-serif;
  }
  .tube-label {
    position: absolute; left: 160px; top: 196px;
    width: 376px; height: 836px;
    background: var(--pack-black);
    border-radius: 6px;
    overflow: hidden;
  }
  .box-front {
    position: absolute; left: 704px; top: 116px;
    width: 348px; height: 924px;
    background: var(--pack-black);
    overflow: hidden;
  }
  .brand-band { position: absolute; left: 0; top: 0; }
  .brand-name { font-family: "Marcellus", serif; fill: var(--ink); letter-spacing: 1px; }
  .brand-sub { font-family: "Poiret One", sans-serif; fill: var(--label-white); letter-spacing: 2px; }
  .brand-tm { font-family: "Open Sans", sans-serif; fill: var(--ink); font-size: 10px; }
  .tube-badge {
    position: absolute; left: 126px; top: 364px;
    width: 124px; height: 124px; border-radius: 50%;
    background: var(--label-white);
    display: flex; flex-direction: column; align-items: center; justify-content: center;
    color: var(--ink); text-align: center; line-height: 1.05;
  }
  .badge-mark {
    width: 14px; height: 14px; border: 2px solid var(--ink); border-radius: 50%;
    margin-bottom: 8px;
  }
  .tube-badge .line-1 { font-size: 15px; letter-spacing: 0.5px; }
  .tube-badge .line-2 { font-size: 10.5px; letter-spacing: 0.3px; margin: 2px 0; }
  .tube-badge .line-3 { font-size: 24px; font-weight: 600; letter-spacing: 1.5px; }
  .product-title {
    position: absolute; left: 44px; top: 288px;
    width: 304px; height: 84px;
    background: var(--charcoal-panel);
    color: var(--panel-text);
    font-family: "Poiret One", sans-serif;
    font-size: 23px; letter-spacing: 1px; line-height: 29px;
    padding: 14px 0 0 20px;
  }
  .box-badge {
    position: absolute; left: 214px; top: 342px;
    width: 134px; height: 62px;
    background: var(--label-white);
    display: flex; align-items: center;
    padding-left: 9px;
  }
  .box-badge .badge-mark { margin: 0 8px 0 0; border-color: #555; }
  .box-badge .tagline { color: var(--accent-red); line-height: 1.05; text-align: center; }
  .box-badge .line-1 { font-size: 12.5px; letter-spacing: 0.6px; display: block; }
  .box-badge .line-2 { font-size: 8.5px; display: block; margin: 1px 0; }
  .box-badge .line-3 { font-size: 21px; font-weight: 600; letter-spacing: 1.5px; display: block; }
  .hero-visual {
    position: absolute; left: 0; top: 420px;
    width: 348px; height: 504px;
    background:
      radial-gradient(ellipse 60% 40% at 50% 20%, #f2f2f2 0%, rgba(230,230,230,0.6) 50%, rgba(0,0,0,0) 100%),
      linear-gradient(180deg, #0a0a0a 0%, #bdbdbd 22%, #eeeeee 40%, #d9b7a3 62%, #e8c9b6 100%);
  }
  .volume {
    position: absolute; right: 14px; bottom: 14px;
    font-family: "Marcellus", serif; font-size: 17px; color: var(--ink);
  }
  .volume small { font-size: 10px; }
</style>
</head>
<body>

  <section class="tube-label" aria-label="Tube label">
    <svg class="brand-band" width="376" height="400" viewBox="0 0 376 400">
      <polygon points="0,126 376,-30 376,60 0,236" fill="var(--label-white)"/>
      <g transform="translate(40 219) rotate(-22.5)">
        <text class="brand-name" x="24" y="-30" font-size="36">FJELLMOSS</text>
        <text class="brand-tm" x="236" y="-56">TM</text>
        <text class="brand-sub" x="40" y="44" font-size="40">BOTANICS</text>
      </g>
    </svg>
    <div class="tube-badge">
      <span class="badge-mark"></span>
      <span class="line-1">RESTORES</span>
      <span class="line-2">YOUR YOUTHFUL</span>
      <span class="line-3">GLOW</span>
    </div>
  </section>

  <section class="box-front" aria-label="Box front panel">
    <svg class="brand-band" width="348" height="286" viewBox="0 0 348 286">
      <polygon points="0,130 348,-14 348,100 0,244" fill="var(--label-white)"/>
      <line x1="0" y1="130" x2="348" y2="-14" stroke="var(--accent-blue)" stroke-width="3"/>
      <line x1="0" y1="244" x2="348" y2="100" stroke="var(--accent-red)" stroke-width="3"/>
      <g transform="translate(20 236) rotate(-22.5)">
        <text class="brand-name" x="14" y="-32" font-size="40">FJELLMOSS</text>
        <text class="brand-tm" x="268" y="-62">TM</text>
        <text class="brand-sub" x="44" y="46" font-size="42">BOTANICS</text>
      </g>
    </svg>
    <div class="product-title">CHARCOAL ACTIVATED<br>FACE MASK</div>
    <div class="box-badge">
      <span class="badge-mark"></span>
      <span class="tagline">
        <span class="line-1">RESTORES</span>
        <span class="line-2">YOUR YOUTHFUL</span>
        <span class="line-3">GLOW</span>
      </span>
    </div>
    <div class="hero-visual" role="img" aria-label="Photograph of a person peeling off a face mask painted with the Norwegian flag, against a white powder splash"></div>
    <div class="volume">50 <small>ML</small></div>
  </section>

</body>
</html>
```